依頼詳細
当院がこの度4月より、木曜診療・駐車場提携・CT導入をしたため、そのお知らせのチラシを作成いただきたいです。(A4裏表)
ラフ・素材等はございます。HP(http://mk-dental.net/)取っていただいても構いません。

※発送はポミネオ様で行う予定です。(https://pomineo.com/directmail/large-sized-postcard/
※まず表面案だけで構いませんのでお出しいただけますと幸いです。その後当選の方が決まり次第裏面もお願いしようと思います。
記載項目
添付ラフ通り
サイズ
A4
ページ数
両面
希望イメージ
シンプル 複雑
単色 カラフル
暗い 明るい
日常 高級
遊び心 厳粛
未来的 伝統的
女性的 男性的
希望する色
緑系
納品ファイル
• イラストレーター形式 (.ai)
• PNG形式 (.png)
補足説明
ポミネオのDM(https://pomineo.com/directmail/large-sized-postcard/)で患者様に発送するため、ポミネオの規定で作成願えますでしょうか。
■ 選んだ理由

全体的なデザインバランスが良かったため

■ 提案者全員のお礼・コメント

この度はご参加いただきまして誠に有難うございました!
今後とも宜しくお願いいたします。

```html
<!DOCTYPE html>
<html lang="ja">
<head>
<meta charset="utf-8">
<title>森川町ファミリー歯科 3つのお知らせ</title>
<link rel="stylesheet" href="https://fonts.googleapis.com/css2?family=Noto+Sans+JP:wght@400;500;700;900&family=M+PLUS+Rounded+1c:wght@700;800&display=swap">
<style>
  :root {
    --green: #6fb52c;
    --green-dark: #3f8a1e;
    --green-pale: #e3f0cf;
    --ink: #333333;
    --red: #e60012;
    --white: #ffffff;
    --pin-1: #3aa0d8;
    --pin-2: #e8572a;
    --pin-3: #8bc34a;
    --pin-4: #f2a81d;
    --pin-5: #9c6fc2;
    --art: #dfeccd;
  }
  * { margin: 0; padding: 0; box-sizing: border-box; }
  html, body { width: 849px; height: 1200px; overflow: hidden; }
  body {
    font-family: "Noto Sans JP", sans-serif;
    color: var(--ink);
    background: var(--green-pale);
  }
  p { line-height: 1.2; }
  .flyer { position: relative; width: 849px; height: 1200px; overflow: hidden; background: var(--green-pale); }

  /* header */
  .header { position: absolute; left: 0; top: 0; width: 849px; height: 320px;
    background: repeating-linear-gradient(135deg, var(--green-pale) 0 10px, #d9eabf 10px 12px); }
  .big-three { position: absolute; left: 28px; top: -8px; font-family: "M PLUS Rounded 1c", sans-serif;
    font-size: 330px; font-weight: 800; line-height: 1; color: var(--white);
    -webkit-text-stroke: 10px var(--green); paint-order: stroke fill; }
  .headline { position: absolute; left: 250px; top: 150px; font-family: "M PLUS Rounded 1c", sans-serif;
    font-weight: 800; font-size: 78px; line-height: 1.1; color: var(--green-dark); }
  .headline span { display: block; }
  .headline .row2 { padding-left: 10px; }
  .mascot-head { position: absolute; left: 170px; top: 26px; width: 150px; height: 130px; border-radius: 40px; background: var(--white); opacity: .9; }

  .info-box { position: absolute; right: 28px; top: 18px; width: 300px; }
  .clinic-name { background: var(--white); border-radius: 6px; padding: 8px 12px; display: flex; align-items: center; gap: 8px;
    font-weight: 700; font-size: 21px; color: var(--green-dark); }
  .clinic-name .mark { width: 20px; height: 20px; border-radius: 50%; background: var(--green); }
  .info-label { margin-top: 8px; background: var(--green); color: var(--white); font-weight: 700; font-size: 22px; text-align: center; padding: 6px 0; letter-spacing: .08em; }
  .info-text { background: var(--white); border: 3px solid var(--green); border-top: none; padding: 10px 0 12px; text-align: center;
    color: var(--green-dark); font-weight: 700; font-size: 18px; line-height: 1.45; }

  /* sections */
  .notice { position: absolute; left: 24px; width: 801px; background: var(--white); border-radius: 6px; }
  .tag { position: absolute; left: 14px; top: 14px; background: var(--green); color: var(--white); font-size: 15px; font-weight: 700;
    padding: 3px 12px; border-radius: 3px; }
  .art { position: absolute; background: var(--art); border-radius: 12px; }

  .notice-1 { top: 336px; height: 126px; }
  .notice-1 .art { left: 24px; top: 44px; width: 110px; height: 70px; }
  .notice-1 .date { position: absolute; left: 170px; top: 16px; font-size: 34px; font-weight: 700; color: var(--green-dark); }
  .notice-1 .lead { position: absolute; left: 170px; top: 58px; font-size: 37px; font-weight: 900; white-space: nowrap; }
  .notice-1 .lead em { font-style: normal; color: var(--red); }
  .notice-1 .note { position: absolute; left: 172px; top: 106px; font-size: 11px; }

  .notice-2 { top: 474px; height: 328px; }
  .notice-2 .art.mascot { left: 24px; top: 54px; width: 110px; height: 110px; }
  .notice-2 .art.car { left: 24px; top: 212px; width: 150px; height: 100px; }
  .notice-2 h2 { position: absolute; left: 170px; top: 18px; font-size: 36px; font-weight: 900; color: var(--green-dark); line-height: 1.2; }
  .notice-2 .sub { position: absolute; left: 172px; top: 70px; font-size: 16px; font-weight: 700; }
  .lots { position: absolute; left: 182px; top: 102px; list-style: none; width: 296px; }
  .lots li { display: flex; align-items: center; height: 36px; font-size: 16px; font-weight: 700; white-space: nowrap; }
  .lots svg { width: 22px; height: 28px; margin-right: 8px; flex: none; }
  .lots .name { flex: 1; }
  .lots .walk { font-size: 12px; font-weight: 500; }
  .lots .walk b { font-size: 17px; }
  .map { position: absolute; left: 494px; top: 74px; width: 286px; height: 220px; background: #eef0ea; border: 1px solid #cfd4c8; }
  .notice-2 .note { position: absolute; left: 210px; top: 302px; font-size: 11px; }

  .notice-3 { top: 816px; height: 384px; border-radius: 6px 6px 0 0; }
  .notice-3 h2 { position: absolute; left: 170px; top: 20px; font-size: 36px; font-weight: 900; color: var(--green-dark); line-height: 1.2; }
  .merit { position: absolute; left: 170px; top: 86px; width: 420px; font-size: 12.5px; }
  .merit h3 { font-size: 17px; font-weight: 700; color: var(--green-dark); margin-bottom: 4px; }
  .merit p { text-indent: -1em; padding-left: 1em; line-height: 1.75; }
  .notice-3 .art { left: 600px; top: 80px; width: 180px; height: 280px; }
</style>
</head>
<body>
<main class="flyer">
  <header class="header">
    <div class="mascot-head art" role="img" aria-label="ピースサインをする歯のキャラクターのイラスト"></div>
    <div class="big-three">3</div>
    <h1 class="headline"><span>つの</span><span class="row2">お知らせ</span></h1>
    <div class="info-box">
      <div class="clinic-name"><span class="mark"></span>森川町ファミリー歯科</div>
      <div class="info-label">インフォメーション</div>
      <div class="info-text">当医院が、<br>少しだけ新しく便利に<br>なります。</div>
    </div>
  </header>

  <section class="notice notice-1">
    <span class="tag">お知らせ1</span>
    <div class="art" role="img" aria-label="歯のキャラクターのイラスト"></div>
    <p class="date">2020年4月1日より</p>
    <p class="lead"><em>木曜日</em>の診療を開始します。</p>
    <p class="note">※休診日：日曜・祝日</p>
  </section>

  <section class="notice notice-2">
    <span class="tag">お知らせ2</span>
    <div class="art mascot" role="img" aria-label="ピースサインをする歯のキャラクターのイラスト"></div>
    <div class="art car" role="img" aria-label="車に乗った家族のイラスト"></div>
    <h2>駐車場が増えました。</h2>
    <p class="sub">ご来院がしやすくなりました！</p>
    <ul class="lots">
      <li><svg viewBox="0 0 22 28"><path d="M11 27C4 17 1 13 1 10a10 10 0 0 1 20 0c0 3-3 7-10 17z" fill="var(--pin-1)"/><circle cx="11" cy="10" r="4" fill="#fff"/></svg><span class="name">パークス森川町</span><span class="walk">徒歩<b>2</b>分</span></li>
      <li><svg viewBox="0 0 22 28"><path d="M11 27C4 17 1 13 1 10a10 10 0 0 1 20 0c0 3-3 7-10 17z" fill="var(--pin-2)"/><circle cx="11" cy="10" r="4" fill="#fff"/></svg><span class="name">パークス森川町東第2</span><span class="walk">徒歩<b>4</b>分</span></li>
      <li><svg viewBox="0 0 22 28"><path d="M11 27C4 17 1 13 1 10a10 10 0 0 1 20 0c0 3-3 7-10 17z" fill="var(--pin-3)"/><circle cx="11" cy="10" r="4" fill="#fff"/></svg><span class="name">パークス森川町2丁目第3</span><span class="walk">徒歩<b>3</b>分</span></li>
      <li><svg viewBox="0 0 22 28"><path d="M11 27C4 17 1 13 1 10a10 10 0 0 1 20 0c0 3-3 7-10 17z" fill="var(--pin-4)"/><circle cx="11" cy="10" r="4" fill="#fff"/></svg><span class="name">パークス森川町2丁目第2</span><span class="walk">徒歩<b>3</b>分</span></li>
      <li><svg viewBox="0 0 22 28"><path d="M11 27C4 17 1 13 1 10a10 10 0 0 1 20 0c0 3-3 7-10 17z" fill="var(--pin-5)"/><circle cx="11" cy="10" r="4" fill="#fff"/></svg><span class="name">パークス森川町2丁目第4</span><span class="walk">徒歩<b>3</b>分</span></li>
    </ul>
    <div class="map" role="img" aria-label="医院と提携駐車場の位置を示す周辺地図"></div>
    <p class="note">※40分〜60分無料駐車券によって異なります</p>
  </section>

  <section class="notice notice-3">
    <span class="tag">お知らせ3</span>
    <h2>歯科用CT導入しました。</h2>
    <div class="merit">
      <h3>CTのメリット</h3>
      <p>・レントゲン撮影だけでは見えない部分まで立体的に確認でき、より正確な診断に役立ちます。</p>
      <p>①根管治療の際に病巣の位置や大きさを把握しやすくなります。</p>
      <p>②親知らずの抜歯前に神経や血管との距離を確認できます。</p>
      <p>③インプラント治療で骨の厚みや高さを正確に測れます。</p>
      <p>④歯周病の進行具合を詳しく調べることができます。</p>
      <p>⑤被ばく量が少なく、短時間で撮影が終わるため安心です。</p>
    </div>
    <div class="art" role="img" aria-label="歯科用CT装置の写真"></div>
  </section>
</main>
</body>
</html>
```